Cover for "ROOTED! The skill and rhythm of guiding teams through calm and delight"

My first book for a global audience of modern performance leaders needs its cover!
I am an international executive coach and I've developed a new approach to replace classic Performance Management with a natural, sustainable approach fit for human beings :) My first book is about this approach and serves two purposes: helping leaders and sparking their curiosity to learn more, and positioning myself as a thought leader in the field.
The book is built on personal experience; it is both professional and personal ("From me to You"), and I'd like to position it beyond classic categorisation.
Its cover should communicate humanness, naturalness, ease and joy, within an unmistakably business-y context. I would like to see designs that use the color yellow (but not sure it communicates the right things).
Updates

Target Market(s)

Leaders who aspire to have a positive impact and deliver results in a meaningful way

Industry/Entity Type

Consulting & Executive Coaching - Trusted Advisor

Font styles to use
Other font styles liked:
• Helvetica Neue

Colors
0094D4
00A9DD
6FCCEA
C7EBF8
E9F6FB
FFC000
F8CF3A
FAE287
FDF2CF
FEFAEE
EE7325
F08F49
F5BC92
FAE3D3
FDF4ED

Requirements
Must have
• A both-and feeling to it (see description), e.g., masculine AND feminine, business AND humanness. Power with, not power over...
Should not have
• Too much "bling" - no classic status symbol business success language

```html
<!DOCTYPE html>
<html lang="en">
<head>
<meta charset="utf-8">
<title>ROOTED – Book Cover</title>
<link rel="stylesheet" href="https://fonts.googleapis.com/css2?family=Inter:wght@500;600;700&display=swap">
<style>
  :root {
    --ink: #000000;
    --sun: #FFD60A;
    --paper: #FFFFFF;
  }
  html, body {
    margin: 0;
    padding: 0;
    width: 751px;
    height: 1200px;
    overflow: hidden;
    background: var(--ink);
  }
  .cover {
    display: block;
    width: 751px;
    height: 1200px;
  }
  .cover__background { fill: var(--ink); }
  .cover__author {
    font-family: "Inter", "Helvetica Neue", Arial, sans-serif;
    font-weight: 500;
    font-size: 31px;
    fill: var(--sun);
  }
  .cover__portrait { fill: var(--sun); }
  .cover__title {
    font-family: "Inter", "Helvetica Neue", Arial, sans-serif;
    font-weight: 600;
    font-size: 160px;
    fill: var(--paper);
  }
  .cover__subtitle {
    font-family: "Inter", "Helvetica Neue", Arial, sans-serif;
    font-weight: 500;
    font-size: 46px;
    fill: var(--paper);
  }
  .cover__band { fill: var(--sun); }
  .cover__tagline {
    font-family: "Inter", "Helvetica Neue", Arial, sans-serif;
    font-weight: 700;
    font-size: 18px;
    fill: var(--ink);
  }
</style>
</head>
<body>
<svg class="cover" viewBox="0 0 751 1200" xmlns="http://www.w3.org/2000/svg">
  <rect class="cover__background" x="0" y="0" width="751" height="1200"/>

  <text class="cover__author" x="375.5" y="96" text-anchor="middle" textLength="410" lengthAdjust="spacing">MARTA ELVSBERG</text>

  <circle class="cover__portrait" cx="377" cy="597" r="292" role="img" aria-label="Silhouette of a person in profile, backlit by a round yellow light"/>

  <text class="cover__title" x="28" y="480" textLength="695" lengthAdjust="spacingAndGlyphs">ROOTED</text>

  <g class="cover__subtitle-group">
    <text class="cover__subtitle" x="36" y="586" textLength="680" lengthAdjust="spacingAndGlyphs">THE SKILL AND RHYTHM OF</text>
    <text class="cover__subtitle" x="36" y="640" textLength="680" lengthAdjust="spacingAndGlyphs">GUIDING TEAMS THROUGH</text>
    <text class="cover__subtitle" x="36" y="694" textLength="680" lengthAdjust="spacingAndGlyphs">CALM AND DELIGHT</text>
  </g>

  <rect class="cover__band" x="0" y="987" width="751" height="123"/>
  <g class="cover__tagline-group">
    <text class="cover__tagline" x="375.5" y="1030" text-anchor="middle" textLength="522" lengthAdjust="spacing">PERFORMANCE MANAGEMENT WITH</text>
    <text class="cover__tagline" x="375.5" y="1058" text-anchor="middle" textLength="625" lengthAdjust="spacing">A NATURAL AND SUSTAINABLE APPROACH</text>
    <text class="cover__tagline" x="375.5" y="1086" text-anchor="middle" textLength="355" lengthAdjust="spacing">FIT FOR HUMAN BEINGS</text>
  </g>
</svg>
</body>
</html>
```